Hypnotherapy- past life regression-life between lives therapist needs a website

I need a website that is enticing and spiritual in its feeling. It needs to have a lot of beautiful nature pictures included. The theme is "Willowmere Hollow- what could you uncover....Tides Lanterns Compass"
Because all of us have the answers to living our best life, they are in our subconcious. But not everyone is capable of accessing them. Hypnosis accesses the subconcious and helps to create new neural pathways in the brain which can create new behaviors and responses to situations.
Hypnosis can help with anxiety, pain relief, weight loss, smoking/vaping cessation, self confidence......anything about yourself that you want to change.
Exploration of past lives and life between lives can reveal things related to ones current life. For example, perhaps your fear of deep water is a result of drowning in a past life. Once this has been discovered, it can lead to changes in ones current life.
Almost any personal behavior one wants to change, can be helped through hypnotherapy.
I need a page for testimonials, a place for scheduling (I will have a link to my scheduling app) some information about hypnotherapy.
I am uploading my logo files. My business card will be using the black and gold style, but my website does not have to reflect that. It can be based on the caramel and deep green like full color logo. Earthy, calm colors.
I also like the mock up of my logo on the beach and there was one on a starry night sky that I also liked.
Target Market(s)
men and women ages 25-50
Industry/Entity Type
natural health and wellness, spirituality
Number of Pages Required
4 page
Requirements
Must have
- a page for testimonials, perhaps with a beautiful nature picture with each one, I will have approximately 6. A link to schedule a complimentary intro session, preferably on the first page
Should not have
- no swinging watches or other sterotyped hypnosis symbols

```html
<!DOCTYPE html>
<html lang="en">
<head>
<meta charset="utf-8">
<title>Willowmere Hollow — Hypnotherapy</title>
<link rel="stylesheet" href="https://fonts.googleapis.com/css2?family=Cinzel:wght@500;700&family=Noto+Serif:ital,wght@0,400;0,700;1,400&display=swap">
<style>
:root{
  --olive:#5f5f35;
  --olive-dark:#2a2a18;
  --gold:#f0b000;
  --gold-soft:#b9ae45;
  --cream:#f4f1e6;
  --ink:#1d1d1d;
  --white:#ffffff;
}
*{margin:0;padding:0;box-sizing:border-box}
html,body{width:1200px;height:2221px;overflow:hidden}
body{position:relative;font-family:"Noto Serif",Georgia,serif;color:var(--ink);background:var(--white)}
.abs{position:absolute}
.heading{font-family:"Cinzel",Georgia,serif;font-variant:small-caps;font-weight:700}

/* hero */
.hero{left:0;top:0;width:1200px;height:664px;
  background:radial-gradient(ellipse at 62% 30%,#7f8f8a 0%,#3f4c48 22%,transparent 50%),
  linear-gradient(100deg,#0b0d0c 0%,#1c241f 35%,#2c3a32 60%,#3a2a3c 100%)}
.nav{left:0;top:0;width:1200px;height:86px;background:rgba(30,30,30,.55);box-shadow:0 2px 6px rgba(0,0,0,.4)}
.brand{left:30px;top:30px;display:flex;align-items:center;gap:6px;color:var(--gold);font-size:11px;font-weight:700}
.brand-dot{width:20px;height:20px;border-radius:50%;background:var(--gold)}
.nav-link{top:30px;font-family:"Cinzel",Georgia,serif;font-variant:small-caps;font-weight:700;font-size:17px;color:var(--gold-soft);letter-spacing:.5px}
.nav-link.active{color:#e8d79a}
.nav-link.active::after{content:"";position:absolute;left:3px;right:3px;top:24px;height:2px;background:var(--gold)}
.rule{left:63px;top:128px;width:2px;height:494px;background:var(--gold)}
.hero-title{left:133px;top:258px;color:var(--cream);font-family:"Cinzel",Georgia,serif;font-variant:small-caps;font-weight:500;font-size:31px;line-height:42px}
.hero-title .mark{background:var(--olive);padding:0 3px 0 0}
.hero-copy{left:133px;top:350px;width:470px;color:#e4e4e4;font-size:14px;line-height:29px;letter-spacing:.8px}
.btn-outline{left:133px;top:458px;width:133px;height:34px;border:1px solid var(--gold-soft);color:var(--gold-soft);font-size:13px;letter-spacing:.8px;display:flex;align-items:center;justify-content:center;gap:10px;border-radius:2px}
.form-card{left:739px;top:243px;width:291px;height:265px;background:rgba(245,245,245,.92);border-radius:3px;padding:22px 13px}
.form-card p{font-size:16px;line-height:27px;color:#222}
.field{position:relative;margin-top:13px;height:47px;border:1px solid #bbb;border-radius:3px;padding:13px 10px;font-size:14px;color:#222}
.field span{position:absolute;top:-7px;left:10px;font-size:10px;color:#888;background:#f4f4f4;padding:0 3px}
.btn-solid{margin-top:13px;width:155px;height:35px;background:var(--gold-soft);color:#fff;font-size:13px;letter-spacing:.8px;display:flex;align-items:center;justify-content:center;gap:14px;border-radius:2px;box-shadow:0 2px 4px rgba(0,0,0,.3)}

/* about */
.about{left:0;top:664px;width:1200px;height:569px;background:var(--olive)}
.sec-title{width:1200px;text-align:center;color:var(--gold);font-size:30px}
.about-lead{left:80px;top:100px;width:1040px;text-align:center;color:#eee;font-size:14px;line-height:29px;letter-spacing:.8px}
.divider{left:408px;top:226px;width:384px;height:2px;background:#9aa0a0}
.media{left:85px;top:257px;width:267px;height:267px;background:var(--olive-dark);display:flex;align-items:center;justify-content:center}
.expect-title{left:408px;top:262px;width:706px;text-align:center;color:var(--gold);font-size:21px}
.expect{left:408px;top:314px;width:715px;color:#eee;font-size:14px;line-height:29px;letter-spacing:.8px}
.expect p{margin-bottom:18px}

/* testimonial */
.testi-title{left:0;top:1284px;width:1200px;text-align:center;color:var(--olive);font-size:30px}
.card{left:171px;top:1371px;width:858px;height:558px;background:#fff;box-shadow:0 1px 4px rgba(0,0,0,.18);border-radius:3px}
.avatar{left:400px;top:13px;width:56px;height:56px;border-radius:50%;background:#bdbdbd}
.stars{left:0;top:76px;width:858px;text-align:center;color:var(--gold);font-size:19px;letter-spacing:1px}
.card-line{left:0;top:110px;width:858px;height:1px;background:#e2e2e2}
.quote{left:125px;top:129px;width:608px;text-align:center;font-style:italic;font-size:14px;line-height:30px;color:#222}
.quote p{margin-bottom:30px}
.author{left:0;top:515px;width:858px;text-align:center;font-weight:700;font-size:16px}
.arrow{top:290px}

/* footer */
.footer{left:0;top:1985px;width:1200px;height:236px;background:var(--olive)}
.foot-brand{left:90px;top:82px;display:flex;align-items:center;gap:8px;color:#fff;font-size:18px;font-weight:700}
.foot-brand i{width:26px;height:26px;border-radius:50%;border:2px solid #fff;display:block}
.foot-h{top:48px;color:var(--gold);font-size:30px}
.foot-list{color:#eee;font-size:17px;line-height:33px;letter-spacing:.8px}
.foot-list div{display:flex;align-items:center;gap:8px}
</style>
</head>
<body>

<section class="abs hero" role="img" aria-label="Misty forest with sunlight streaming through tall trees"></section>

<header class="abs nav">
  <div class="abs brand"><i class="brand-dot"></i>Willowmere Hollow</div>
  <a class="abs nav-link active" style="left:492px">Home</a>
  <a class="abs nav-link" style="left:603px">Services</a>
  <a class="abs nav-link" style="left:745px">Testimonial</a>
  <a class="abs nav-link" style="left:916px">About Us</a>
  <a class="abs nav-link" style="left:1052px">Contact Us</a>
</header>

<div class="abs rule"></div>
<h1 class="abs hero-title"><span class="mark">Unlock Your Subconscious</span><br>Discover Your Best Self</h1>
<p class="abs hero-copy">Journey through time and find lessons, solutions, and answers within your own mind. Explore the transformative power of hypnotherapy.</p>
<a class="abs btn-outline">LEARN MORE <svg width="8" height="10" viewBox="0 0 8 10"><path d="M2 1l4 4-4 4" fill="none" stroke="currentColor" stroke-width="1.5"/></svg></a>

<form class="abs form-card">
  <p>Ready to transform your life?<br>Schedule your session.</p>
  <div class="field"><span>Full name</span>Full name</div>
  <div class="field" style="margin-top:8px"><span>Email address *</span>Email address</div>
  <div class="btn-solid">SCHEDULE NOW <svg width="8" height="10" viewBox="0 0 8 10"><path d="M2 1l4 4-4 4" fill="none" stroke="#fff" stroke-width="1.5"/></svg></div>
</form>

<section class="abs about">
  <h2 class="abs heading sec-title" style="top:42px">About Us</h2>
  <p class="abs about-lead">Because all of us have the answers to living our best life, they are in our subconcious. But not everyone is capable of accessing them. Hypnosis accesses the subconcious and helps to create new neural pathways in the brain which can create new behaviors and responses to situations.</p>
  <div class="abs divider"></div>
  <div class="abs media" role="img" aria-label="Calm nature photograph">
    <svg width="42" height="42" viewBox="0 0 42 42"><rect x="2" y="2" width="38" height="38" rx="4" fill="none" stroke="#fff" stroke-width="3"/><path d="M8 34l9-11 7 8 4-5 7 8z" fill="#fff"/></svg>
  </div>
  <h3 class="abs heading expect-title">What to Expect?</h3>
  <div class="abs expect">
    <p>Hypnosis can help with anxiety, pain relief, weight loss, smoking/vaping cessation, self confidence......anything about yourself that you want to change.</p>
    <p>Exploration of past lives and life between lives can reveal things related to ones current life. For example, perhaps your fear of deep water is a result of drowning in a past life. Once this has been discovered, it can lead to changes in ones current life.</p>
    <p>Almost any personal behavior one wants to change, can be helped through hypnotherapy.</p>
  </div>
</section>

<h2 class="abs heading testi-title">Testimonial</h2>
<article class="abs card">
  <div class="abs avatar"><svg width="56" height="56" viewBox="0 0 56 56"><circle cx="28" cy="26" r="3.5" fill="#fff"/><path d="M21 35c0-4 3-6 7-6s7 2 7 6z" fill="#fff"/></svg></div>
  <div class="abs stars">★★★★★</div>
  <div class="abs card-line"></div>
  <svg class="abs arrow" style="left:56px" width="24" height="40" viewBox="0 0 24 40"><path d="M20 3L4 20l16 17" fill="none" stroke="#cfca8f" stroke-width="3"/></svg>
  <svg class="abs arrow" style="left:778px" width="24" height="40" viewBox="0 0 24 40"><path d="M4 3l16 17L4 37" fill="none" stroke="#cfca8f" stroke-width="3"/></svg>
  <div class="abs quote">
    <p>"I had the most incredible experience at Willowmere Hollow with Elias. I was initially skeptical about hypnotherapy, but Elias's warm and reassuring demeanor put me at ease from the moment I walked in.</p>
    <p>The session itself was transformative. Elias guided me through a journey into my subconscious, helping me uncover insights and clarity about challenges I had been facing. It was like unlocking a door to a part of myself I never knew existed.</p>
    <p>I sought help for anxiety, and the positive changes have been profound. Elias's expertise and personalized approach made all the difference. I highly recommend Willowmere Hollow to anyone seeking a path to self-discovery and positive change. Thank you, Elias, for your guidance and support!"</p>
  </div>
  <div class="abs author">Maren T.</div>
</article>

<footer class="abs footer">
  <div class="abs foot-brand"><i></i>Willowmere Hollow</div>
  <h4 class="abs heading foot-h" style="left:480px">Links</h4>
  <div class="abs foot-list" style="left:480px;top:88px">
    <div>Our Programs</div><div>About Us</div><div>Contact Us</div>
  </div>
  <h4 class="abs heading foot-h" style="left:897px">Contact Us</h4>
  <div class="abs foot-list" style="left:897px;top:88px">
    <div><svg width="16" height="16" viewBox="0 0 16 16"><path d="M3 1.5l3 1 .5 3-2 1.2a9 9 0 004.8 4.8l1.2-2 3 .5 1 3c-1 1.3-2.5 1.8-4 1.3A12 12 0 011.7 5.5C1.2 4 1.7 2.5 3 1.5z" fill="none" stroke="#fff" stroke-width="1.3"/></svg>Phone: +1 555 0142</div>
    <div><svg width="17" height="14" viewBox="0 0 17 14"><rect x="1" y="1.5" width="15" height="11" fill="none" stroke="#fff" stroke-width="1.3"/><path d="M1 2l7.5 6L16 2" fill="none" stroke="#fff" stroke-width="1.3"/></svg>Email: hello@willowmere.example</div>
  </div>
</footer>

</body>
</html>
```